Business Card Design Project

We need a Business Card for an Mechanical Engineering firm in Singapore. The design should be Modern & Technical looking, yet eye catching.

Our company deals in Cutting Tools & Machine Accessories for the Manufacturing Industries such as Oil & Gas, Aero Space, etc... For more information on our Company, you can either email me or view our website www.valtrion.com.sg.

We are trying to revamp our image to give our consumers a fresh new perspective to our company, so we welcome all ideas.

Industry/Entity Type

Business

Requirements
Must have
• Must incorporate New Company Logo into the card as shown in Uploaded file.

```html
<!DOCTYPE html>
<html lang="en">
<head>
<meta charset="utf-8">
<title>Valtrion Tools – Business Card</title>
<link href="https://fonts.googleapis.com/css2?family=Signika:wght@400;600&display=swap" rel="stylesheet">
<style>
  :root {
    --maroon: #7d0030;
    --ink: #3b1a29;
    --rule: #8c8089;
    --paper: #ffffff;
  }
  * { margin: 0; padding: 0; box-sizing: border-box; }
  html, body { width: 1200px; height: 763px; overflow: hidden; background: var(--paper); }
  .card {
    position: relative;
    width: 1200px;
    height: 763px;
    background: var(--paper);
    font-family: "Signika", "Trebuchet MS", sans-serif;
    color: var(--ink);
    overflow: hidden;
  }
  .card-graphics { position: absolute; inset: 0; }
  .holder-name {
    position: absolute;
    left: 744px;
    top: 129px;
    font-size: 40px;
    font-weight: 600;
    color: var(--paper);
    line-height: 65px;
    letter-spacing: 0.4px;
    white-space: nowrap;
  }
  .address {
    position: absolute;
    left: 744px;
    top: 269px;
    font-size: 35px;
    line-height: 42px;
    color: var(--ink);
    list-style: none;
    letter-spacing: 1px;
    white-space: nowrap;
  }
  .contacts {
    position: absolute;
    top: 477px;
    left: 0;
    width: 1200px;
    font-size: 35px;
    line-height: 42px;
  }
  .contact-row { position: relative; height: 42px; }
  .contact-label {
    position: absolute;
    right: 506px;
    color: var(--maroon);
  }
  .contact-value {
    position: absolute;
    left: 744px;
    color: var(--ink);
    letter-spacing: 0.6px;
    white-space: nowrap;
  }
  .brand {
    position: absolute;
    left: 110px;
    top: 262px;
    width: 440px;
    text-align: center;
  }
  .brand-dot {
    display: block;
    width: 110px;
    height: 110px;
    margin: 0 auto 18px;
    border-radius: 50%;
    background: var(--maroon);
  }
  .brand-name {
    font-size: 50px;
    font-weight: 400;
    color: var(--maroon);
    letter-spacing: 2px;
    line-height: 60px;
    white-space: nowrap;
  }
</style>
</head>
<body>
  <main class="card">
    <svg class="card-graphics" width="1200" height="763" viewBox="0 0 1200 763" aria-hidden="true">
      <rect class="name-band" x="0" y="129" width="1200" height="65" fill="var(--maroon)"/>
      <line class="divider" x1="718" y1="0" x2="718" y2="763" stroke="var(--rule)" stroke-width="3"/>
    </svg>

    <h1 class="holder-name">Name Surname</h1>

    <div class="brand">
      <span class="brand-dot"></span>
      <div class="brand-name">VALTRION TOOLS</div>
    </div>

    <ul class="address">
      <li>Valtrion Tools Pte Ltd</li>
      <li>27 Kallang Crescent #03-12,</li>
      <li>Meridian Industrial Hub,</li>
      <li>Singapore 339410</li>
    </ul>

    <div class="contacts">
      <div class="contact-row"><span class="contact-label">tel</span><span class="contact-value">65-61234580</span></div>
      <div class="contact-row"><span class="contact-label">fax</span><span class="contact-value">65-61234581</span></div>
      <div class="contact-row"><span class="contact-label">email</span><span class="contact-value">valtrion@valtrion.com.sg</span></div>
      <div class="contact-row"><span class="contact-label">website</span><span class="contact-value">www.valtrion.com.sg</span></div>
    </div>
  </main>
</body>
</html>
```